Ironvale Holdings Business card

We need a an amazing matte black and gold card! W are a finance investing company so we want something that's eye catching and sleek. We want it to be attractive and sleek and represent money. Heck with would like the letters and lgo to be printed as 24k gold one day. We have the logo added so please use the color scheme with the logo and have that beautifully placed on one side.

Target Market(s)

Investors of all ages

Industry/Entity Type

Financial

Contact Information for Business Card

Black and matte with gold lettering follow logo colrs please.

Font styles to use
Other font styles liked:
• you decide

Colors

Designer to choose colors to be used in the design.

Requirements
Must have
• Matte Black and Gold, logo on one side. job title and name , website, phone number and email address on the other side
Nice to have
• Matte black and crisp finish to attract investors
Should not have
• playful, very professional!

```html
<!DOCTYPE html>
<html lang="en">
<head>
<meta charset="UTF-8">
<title>Ironvale Holdings Business Card</title>
<link rel="stylesheet" href="https://fonts.googleapis.com/css2?family=Mulish:wght@400;600;700&display=swap">
<style>
  :root {
    --stage: #1c1c1d;
    --card: #0d0e10;
    --gold: #d9be3f;
    --gold-deep: #a8902a;
    --ink-light: #f2f2f2;
  }
  * { margin: 0; padding: 0; box-sizing: border-box; }
  html, body {
    width: 1200px;
    height: 900px;
    overflow: hidden;
    background: var(--stage);
    font-family: "Mulish", "Century Gothic", sans-serif;
  }
  .stage {
    width: 1200px;
    height: 900px;
    display: flex;
    flex-direction: column;
    align-items: center;
    justify-content: center;
    gap: 40px;
  }
  .card {
    position: relative;
    width: 640px;
    height: 366px;
    background: var(--card);
    box-shadow: 0 14px 30px rgba(0, 0, 0, 0.55);
    display: flex;
    align-items: center;
    justify-content: center;
  }
  .card::after {
    content: "";
    position: absolute;
    left: 0;
    right: 0;
    bottom: 0;
    height: 6px;
    background: linear-gradient(90deg, var(--gold-deep), var(--gold));
  }
  .brand {
    display: flex;
    align-items: center;
    gap: 14px;
    margin-top: -70px;
  }
  .brand-mark {
    width: 14px;
    height: 14px;
    background: var(--gold);
  }
  .brand-name {
    color: var(--gold);
    font-weight: 700;
    font-size: 34px;
    line-height: 1;
  }
  .contact-block {
    display: flex;
    align-items: center;
    gap: 22px;
    margin-top: 20px;
  }
  .person {
    text-align: right;
  }
  .person-name {
    color: var(--gold);
    font-weight: 700;
    font-size: 24px;
    line-height: 1.2;
  }
  .person-title {
    color: var(--ink-light);
    font-size: 17px;
    margin-top: 4px;
  }
  .divider {
    width: 1.5px;
    height: 84px;
    background: var(--gold);
  }
  .details {
    list-style: none;
    display: flex;
    flex-direction: column;
    gap: 8px;
  }
  .details li {
    display: flex;
    align-items: center;
    gap: 10px;
    color: var(--ink-light);
    font-size: 17px;
  }
  .details svg {
    width: 13px;
    height: 13px;
    flex: none;
  }
</style>
</head>
<body>
  <main class="stage">
    <section class="card card-front">
      <div class="brand">
        <span class="brand-mark"></span>
        <span class="brand-name">Ironvale Holdings</span>
      </div>
    </section>

    <section class="card card-back">
      <div class="contact-block">
        <div class="person">
          <p class="person-name">Daniel Hale</p>
          <p class="person-title">Director</p>
        </div>
        <span class="divider"></span>
        <ul class="details">
          <li>
            <svg viewBox="0 0 16 16" aria-hidden="true"><path fill="var(--gold)" d="M3.5 1.5l2.3 2.8-1.3 1.6c.9 2 2.6 3.7 4.6 4.6l1.6-1.3 2.8 2.3-1.4 2.2C7 13.4 2.6 9 1.3 3z"/></svg>
            613-555-0172
          </li>
          <li>
            <svg viewBox="0 0 16 16" aria-hidden="true"><rect x="1" y="3" width="14" height="10" fill="var(--gold)"/><path d="M1.5 3.5L8 9l6.5-5.5" fill="none" stroke="var(--card)" stroke-width="1.4"/></svg>
            info@ironvaleholdings.com
          </li>
          <li>
            <svg viewBox="0 0 16 16" aria-hidden="true"><circle cx="8" cy="8" r="6.5" fill="none" stroke="var(--gold)" stroke-width="1.4"/><ellipse cx="8" cy="8" rx="2.8" ry="6.5" fill="none" stroke="var(--gold)" stroke-width="1.2"/><path d="M1.5 8h13" stroke="var(--gold)" stroke-width="1.2"/></svg>
            www.ironvaleholdings.com
          </li>
        </ul>
      </div>
    </section>
  </main>
</body>
</html>
```